KLR Dental Plan
re-design of a tri-fold brochure for KLR dental plan  - Health
re-design of a tri-fold brochure for KLR dental plan
Health
general public
the font sizes for the terms&conditions (10pt font) and the Disclosures (12pt font) have to be the specific size stated in the details. This Plan is Not available in VT and WA Keep the logo with the line that states " Featuring the Orvix Dental Access Network"
brightmolar brightmolar
Can not increase size of brochure.
Plindor Plindor
My design is 8.5x11 inch size. Please provide feedbacks through private message.
I do not want to increase the size of the brochure. I want it designed to fit on an 8 1/2 x 11 tri-fold.
wexomira wexomira
Dear Project holder, With the size requirements of the terms and condition and Disclosures you may find in beneficial to increase the size of the brochure to a 4pp DL gate-folded brochure like the one found here http://www.mellowprintco.example/store/images/D/brochure-gate-doble-fold-600px-01.jpg. If you could please let me know your thoughts. Much appreciated Tomas
Please could you supply all the copy in Word as it is currently embedded as outlines. Looking forward to working on this piece. Tomas
BrisklyOwlDEV BrisklyOwlDEV
Dear Project Holder, In my opinion, the (female) photo embedded in provided file is not quality enough for redesign & printing. By the way, could you please upload the content again (in M.Word) which can not editable anymore in the file, I'm typing all & seems take too long. Really appreciate! Thank you. BrisklyOwlDEV

```html
<!DOCTYPE html>
<html lang="en">
<head>
<meta charset="utf-8">
<title>KLR Dental Plan – Tri-fold Brochure</title>
<link href="https://fonts.googleapis.com/css2?family=Open+Sans:wght@400;600;700;800&display=swap" rel="stylesheet">
<style>
  :root{
    --bg:#eef0f3;
    --paper:#ffffff;
    --blue:#1f5fae;
    --blue-dark:#16468a;
    --blue-tint:#dce8f6;
    --blue-soft:#eaf1fa;
    --yellow:#f6e21c;
    --ink:#2f3338;
    --muted:#6b7280;
    --rule:#b9c7d8;
  }
  *{box-sizing:border-box;margin:0;padding:0}
  html,body{width:1200px;height:901px;overflow:hidden}
  body{background:var(--bg);font-family:"Open Sans",Arial,sans-serif;color:var(--ink);position:relative}

  .inside-spread{position:absolute;left:50px;top:165px;width:780px;height:570px;display:flex;background:var(--paper);box-shadow:0 6px 18px rgba(0,0,0,.15)}
  .panel{width:260px;height:100%;padding:18px 16px;position:relative;border-right:1px solid #e3e7ec;font-size:7.5px;line-height:1.45}
  .panel:last-child{border-right:none}
  .panel p{margin-bottom:8px}
  .section-bar{background:var(--blue);color:#fff;font-weight:700;font-size:11px;padding:6px 10px;border-radius:0 14px 0 0;margin:12px -16px 10px;}
  .top-band{height:8px;background:var(--blue);margin:-18px -16px 14px}

  .savings-table{width:100%;border-collapse:collapse;font-size:7.5px;margin-bottom:10px}
  .savings-table th{background:var(--blue-dark);color:#fff;font-weight:600;padding:4px 3px;text-align:left}
  .savings-table td{padding:4px 3px;border-bottom:1px solid var(--rule)}
  .savings-table tr:nth-child(even) td{background:var(--blue-soft)}
  .savings-table td.num{text-align:right;color:var(--blue-dark);font-weight:600}
  .quote{background:var(--blue-tint);padding:7px 9px;margin-bottom:7px;font-style:normal;border-left:3px solid var(--blue)}
  .quote cite{display:block;font-style:normal;color:var(--muted);margin-top:2px}

  .form-field{display:flex;align-items:flex-end;gap:5px;margin-bottom:9px;font-size:7.5px}
  .form-field .line{flex:1;border-bottom:1px solid var(--ink);height:9px}
  .checks{display:flex;gap:12px;margin:4px 0 10px}
  .checks span::before{content:"";display:inline-block;width:7px;height:7px;border:1px solid var(--ink);margin-right:4px;vertical-align:-1px}
  .form-note{color:var(--muted);margin-top:8px}

  .cover{position:absolute;left:880px;top:165px;width:270px;height:570px;background:var(--paper);overflow:hidden;box-shadow:0 6px 18px rgba(0,0,0,.15)}
  .cover-stripe{height:10px;background:var(--blue)}
  .brand{text-align:center;padding:26px 10px 10px}
  .brand-name{display:inline-flex;align-items:center;gap:7px;font-size:22px;font-weight:700;color:var(--blue-dark)}
  .brand-name::before{content:"";width:14px;height:14px;border-radius:50%;background:var(--blue-dark)}
  .brand-tag{font-size:8.5px;color:var(--blue-dark);margin-top:4px}
  .cover-photo{position:absolute;left:0;top:120px;width:270px;height:250px;background:linear-gradient(160deg,#e9eef3 0%,#d3dde7 55%,#bfd0e0 100%)}
  .cover-wave{position:absolute;left:0;top:300px;width:270px;height:270px}
  .cover-copy{position:absolute;left:0;right:0;top:400px;text-align:center;color:var(--paper)}
  .headline{color:var(--yellow);font-size:22px;font-weight:800;line-height:1.15;margin-bottom:22px}
  .phone{font-size:16px;font-weight:700}
  .contact{font-size:10px;line-height:1.5;margin-top:4px}
</style>
</head>
<body>

<section class="inside-spread">
  <div class="panel panel-info">
    <div class="top-band"></div>
    <p>Members may take advantage of savings through the Orvix Dental Access Network at the locations shown.</p>
    <p>Participants must pay the dentist directly at the time of service.</p>
    <p>This is a discount plan for members. Savings vary by region and provider.</p>
    <p>Plan is offered through KLR Dental Plan. Not available in VT and WA.</p>
    <div class="section-bar">Disclosures</div>
    <p>This plan is not insurance and is not a Medicare prescription plan. The plan provides discounts at certain health care providers for dental services. The plan does not make payments directly to providers. Members are obligated to pay for all services at the time of service.</p>
  </div>

  <div class="panel panel-savings">
    <div class="section-bar" style="margin-top:0">Sample List of Approximate Savings</div>
    <table class="savings-table">
      <thead><tr><th>Procedure</th><th>Usual</th><th>Member</th><th>Save</th></tr></thead>
      <tbody>
        <tr><td>Routine Cleaning</td><td>$95</td><td>$52</td><td class="num">45%</td></tr>
        <tr><td>Periodic Exam</td><td>$55</td><td>$30</td><td class="num">45%</td></tr>
        <tr><td>Full X-Rays</td><td>$140</td><td>$78</td><td class="num">44%</td></tr>
        <tr><td>Filling, One Surface</td><td>$150</td><td>$88</td><td class="num">41%</td></tr>
        <tr><td>Simple Extraction</td><td>$180</td><td>$104</td><td class="num">42%</td></tr>
        <tr><td>Root Canal</td><td>$980</td><td>$610</td><td class="num">38%</td></tr>
        <tr><td>Crown</td><td>$1,150</td><td>$720</td><td class="num">37%</td></tr>
        <tr><td>Night Guard</td><td>$560</td><td>$330</td><td class="num">41%</td></tr>
      </tbody>
    </table>
    <div class="section-bar">What our members are saying…</div>
    <blockquote class="quote">“Great savings on my family's cleanings.”<cite>– Satisfied Member</cite></blockquote>
    <blockquote class="quote">“Easy to use and my dentist was listed.”<cite>– Plan Member</cite></blockquote>
  </div>

  <div class="panel panel-form">
    <div class="section-bar" style="margin-top:0">Dental Plan Application</div>
    <div class="form-field">Name<span class="line"></span></div>
    <div class="form-field">Address<span class="line"></span></div>
    <div class="form-field">City<span class="line"></span>State<span class="line"></span></div>
    <div class="form-field">Zip<span class="line"></span>Phone<span class="line"></span></div>
    <div class="form-field">Email<span class="line"></span></div>
    <div class="form-field">Date of Birth<span class="line"></span></div>
    <div class="section-bar">Plan Type</div>
    <div class="checks"><span>Individual</span><span>Couple</span><span>Family</span></div>
    <div class="form-field">Spouse Name<span class="line"></span></div>
    <div class="form-field">Dependent<span class="line"></span></div>
    <div class="section-bar">Payment</div>
    <div class="form-field">Card Number<span class="line"></span></div>
    <div class="form-field">Exp. Date<span class="line"></span>Signature<span class="line"></span></div>
    <p class="form-note">Mail completed form to KLR Dental Plan.</p>
  </div>
</section>

<section class="cover">
  <div class="cover-stripe"></div>
  <div class="brand">
    <div class="brand-name">KLR Dental Plan</div>
    <div class="brand-tag">Featuring the Orvix Dental Access Network</div>
  </div>
  <div class="cover-photo" role="img" aria-label="Photo of a smiling dental professional in a white coat"></div>
  <svg class="cover-wave" viewBox="0 0 270 270" aria-hidden="true">
    <path d="M0 60 C90 20 180 10 270 40 L270 270 L0 270 Z" fill="var(--blue-tint)"/>
    <path d="M0 80 C90 45 180 40 270 70 L270 270 L0 270 Z" fill="var(--blue)"/>
  </svg>
  <div class="cover-copy">
    <div class="headline">Save On Dental<br>Costs Today!</div>
    <div class="phone">800-555-0142</div>
    <div class="contact">info@klrdental.example<br>www.klrdental.example</div>
  </div>
</section>

</body>
</html>
```